Willowmere Counseling (Endure - Mend - Flourish) - Double Sided Business Card

I would like a 2-sided business card. Front: Matte Black or Navy with Logo & Tagline. Back: Name, Address, Phone Number, Email, & Website (maybe would like to include a small map pin-pointing location); Prefer front to be a gold/silver foil (iridescent); Back prefer white or light colored background with lettering that is easy to read and simple

Target Market(s)

Individuals & Couples (13 y.o. - ALL Adults); High end clientele

Industry/Entity Type

Licensed Professional Counselor (Mental Health)

Contact Information for Business Card

Name: Willowmere Counseling; Tagline: Endure - Mend - Flourish; Address: 3870 N. Garrick Ave., Suite 214, Fort Worth, TX 76132; Phone: (214) 555-0187; Website: www.WillowmereCounseling.example

Font styles to use
Serif

Requirements
Must have
• Logo on Front (Large) prefer gold/silver foil on a matte dark color (i.e. black, navy, etc.); Back of Card: All other relevant information

```html
<!DOCTYPE html>
<html lang="en">
<head>
<meta charset="utf-8">
<title>Willowmere Counseling – Business Card</title>
<link rel="stylesheet" href="https://fonts.googleapis.com/css2?family=Cinzel:wght@500&family=Lora:wght@400&display=swap">
<style>
  :root {
    --backdrop: #5b5b5b;
    --navy: #1a1f35;
    --gold: #d8b85a;
    --silver: #8a8b90;
    --paper: #ffffff;
    --ink: #2a2a2a;
  }
  * { margin: 0; padding: 0; box-sizing: border-box; }
  html, body {
    width: 1200px;
    height: 1195px;
    overflow: hidden;
  }
  body {
    position: relative;
    background: var(--backdrop);
  }
  .card {
    position: absolute;
    left: 238px;
    width: 724px;
    height: 438px;
  }
  .card-front {
    top: 135px;
    background: var(--navy);
  }
  .card-back {
    top: 635px;
    background: var(--paper);
  }
  .brand-mark {
    position: absolute;
    left: 50%;
    top: 132px;
    width: 80px;
    height: 80px;
    margin-left: -40px;
    border: 5px solid var(--gold);
    border-radius: 50%;
  }
  .brand-name {
    position: absolute;
    left: 0;
    right: 0;
    top: 224px;
    text-align: center;
    font-family: "Cinzel", serif;
    font-weight: 500;
    font-size: 26px;
    letter-spacing: 1px;
    color: var(--gold);
  }
  .brand-tagline {
    position: absolute;
    left: 0;
    right: 0;
    top: 274px;
    text-align: center;
    font-family: "Cinzel", serif;
    font-weight: 500;
    font-size: 12px;
    letter-spacing: 0.5px;
    color: var(--gold);
  }
  .back-title {
    position: absolute;
    left: 0;
    right: 0;
    top: 120px;
    text-align: center;
    font-family: "Cinzel", serif;
    font-weight: 500;
    font-size: 23px;
    letter-spacing: 6px;
    color: var(--gold);
  }
  .contact-line {
    position: absolute;
    left: 0;
    right: 0;
    text-align: center;
    font-family: "Lora", serif;
    font-size: 12px;
    color: var(--ink);
  }
  .contact-phone { top: 212px; }
  .contact-address { top: 237px; }
  .contact-web { top: 338px; }
</style>
</head>
<body>
  <section class="card card-front">
    <div class="brand-mark"></div>
    <h1 class="brand-name">Willowmere Counseling</h1>
    <p class="brand-tagline">Endure - Mend - Flourish</p>
  </section>

  <section class="card card-back">
    <h2 class="back-title">WILLOWMERE COUNSELING</h2>
    <p class="contact-line contact-phone">phone: (214) 555-0187</p>
    <p class="contact-line contact-address">address: 3870 N. Garrick Ave., Suite 214, Fort Worth, TX 76132</p>
    <p class="contact-line contact-web">website: www.WillowmereCounseling.example</p>
  </section>
</body>
</html>
```